Bref créative
Karvelo ApS wants a cool new identity on stationary
Total outline for the stationary stuff
Simple
Henrik Dahlquist
CEO
Birkeslette 218
5810 Naestved
Denmark
henrik@karvelo.dk
www.karvelo.dk
Free your mind
We want the design to show trust, technology, to be frontrunner, inovation etc. - streamlined with a crisp look.

```html
<!DOCTYPE html>
<html lang="en">
<head>
<meta charset="utf-8">
<title>Karvelo ApS – Stationery</title>
<link rel="stylesheet" href="https://fonts.googleapis.com/css2?family=Open+Sans:wght@400;600&display=swap">
<style>
  :root {
    --backdrop: #363636;
    --paper: #ffffff;
    --brand-green: #8cc63f;
    --ink-dark: #2b2b2b;
    --ink-grey: #8a8a8a;
    --band-dark: #3d3d3d;
    --flap-line: #d4d4d4;
  }
  * { box-sizing: border-box; margin: 0; padding: 0; }
  html, body { width: 1200px; height: 684px; overflow: hidden; }
  body {
    background: var(--backdrop);
    font-family: "Open Sans", Arial, sans-serif;
    position: relative;
  }
  .sheet {
    position: absolute;
    background: var(--paper);
    box-shadow: 0 2px 8px rgba(0,0,0,.35);
    overflow: hidden;
  }
  .wordmark {
    position: absolute;
    display: flex;
    align-items: center;
    gap: 8px;
    color: var(--ink-dark);
    font-weight: 600;
    line-height: 1;
  }
  .wordmark .mark-square {
    background: var(--brand-green);
    display: block;
  }
  .band { position: absolute; left: 0; width: 100%; }
  .band svg { display: block; width: 100%; height: 100%; }
  .band-label {
    position: absolute;
    left: 14px;
    top: 50%;
    transform: translateY(-50%);
    color: var(--paper);
    font-size: 6px;
  }
  .contact-line {
    position: absolute;
    font-size: 5px;
    color: var(--ink-grey);
    white-space: nowrap;
  }

  /* Letterhead */
  .letterhead { left: 187px; top: 24px; width: 473px; height: 636px; }
  .letterhead .wordmark { left: 30px; top: 72px; font-size: 26px; }
  .letterhead .mark-square { width: 22px; height: 22px; }
  .letterhead .contact-line { left: 30px; top: 586px; }
  .letterhead .band { bottom: 10px; height: 16px; }

  /* Business card */
  .business-card { left: 125px; top: 307px; width: 199px; height: 106px; }
  .business-card .wordmark { left: 10px; top: 14px; font-size: 15px; gap: 5px; }
  .business-card .mark-square { width: 12px; height: 12px; }
  .card-details {
    position: absolute; left: 12px; top: 40px;
    font-size: 4.5px; line-height: 1.5; color: var(--ink-grey);
  }
  .card-details .person { color: var(--ink-dark); font-weight: 600; }
  .business-card .band { bottom: 4px; height: 8px; }

  /* Envelope back */
  .envelope-back { left: 643px; top: 108px; width: 413px; height: 180px; }
  .envelope-back svg { position: absolute; inset: 0; }

  /* Envelope front */
  .envelope-front { left: 660px; top: 365px; width: 396px; height: 230px; }
  .envelope-front .wordmark { left: 40px; top: 44px; font-size: 24px; }
  .envelope-front .mark-square { width: 20px; height: 20px; }
  .envelope-front .contact-line { left: 22px; top: 190px; }
  .envelope-front .band { bottom: 14px; height: 14px; }
</style>
</head>
<body>

<section class="sheet letterhead" aria-label="Letterhead">
  <div class="wordmark"><span class="mark-square"></span>Karvelo</div>
  <p class="contact-line">Birkeslette 218, DK-5810 Naestved Denmark &nbsp;|&nbsp; +45 3190 6274 &nbsp;|&nbsp; +45 4067 1583 &nbsp;|&nbsp; henrik@karvelo.dk</p>
  <div class="band">
    <svg viewBox="0 0 473 16" preserveAspectRatio="none">
      <polygon points="0,0 405,0 390,16 0,16" fill="var(--brand-green)"/>
      <polygon points="405,0 473,0 473,16 390,16" fill="var(--band-dark)"/>
    </svg>
    <span class="band-label">www.karvelo.dk</span>
  </div>
</section>

<section class="sheet business-card" aria-label="Business card">
  <div class="wordmark"><span class="mark-square"></span>Karvelo</div>
  <div class="card-details">
    <p class="person">Henrik Dahlquist</p>
    <p>CEO</p>
    <p>Tel +45 3190 6274</p>
    <p>Mob +45 4067 1583</p>
    <p>henrik@karvelo.dk</p>
  </div>
  <div class="band">
    <svg viewBox="0 0 199 8" preserveAspectRatio="none">
      <polygon points="0,0 150,0 142,8 0,8" fill="var(--brand-green)"/>
      <polygon points="150,0 199,0 199,8 142,8" fill="var(--band-dark)"/>
    </svg>
  </div>
</section>

<section class="sheet envelope-back" aria-label="Envelope back">
  <svg viewBox="0 0 413 180" preserveAspectRatio="none">
    <polyline points="0,0 206,62 413,0" fill="none" stroke="var(--flap-line)" stroke-width="1.2"/>
    <line x1="0" y1="180" x2="150" y2="80" stroke="var(--flap-line)" stroke-width="1"/>
    <line x1="413" y1="180" x2="263" y2="80" stroke="var(--flap-line)" stroke-width="1"/>
  </svg>
</section>

<section class="sheet envelope-front" aria-label="Envelope front">
  <div class="wordmark"><span class="mark-square"></span>Karvelo</div>
  <p class="contact-line">Birkeslette 218, DK-5810 Naestved Denmark &nbsp;|&nbsp; +45 3190 6274 &nbsp;|&nbsp; +45 4067 1583 &nbsp;|&nbsp; henrik@karvelo.dk</p>
  <div class="band">
    <svg viewBox="0 0 396 14" preserveAspectRatio="none">
      <polygon points="0,0 340,0 326,14 0,14" fill="var(--brand-green)"/>
      <polygon points="340,0 396,0 396,14 326,14" fill="var(--band-dark)"/>
    </svg>
    <span class="band-label">www.karvelo.dk</span>
  </div>
</section>

</body>
</html>
```